High-Converting Facebook Ads for Panes Screens & Louvres (6 Products)

We are looking for a graphic designer to create high-quality Facebook & Instagram ads for our business: Panes Screens and Louvres (Melbourne, Australia).

We require 6 separate ad designs, each for a different product:

Veltrashade Blinds

Outdoor Awnings

Plantation Shutters

Roller Shutters

Security Doors

Roller Blinds & Sheer Curtains

Ad Specifications:

Sizes:

1440 x 1800 px (4:5 ratio)

1080 x 1080 px (1:1 ratio)

1080 x 1920 px (9:16 ratio for Stories/Reels)

Format: PNG (high resolution, not blurry)

Designed specifically for Meta (Facebook/Instagram ads)

Mobile-friendly layout (clear, easy to read)

Style:

Bold, sales-driven, retail-style ads (NOT minimal)

Eye-catching and designed to generate leads

Clean, professional layout

Similar to promotional home improvement ads

Brand Colours:

Red: #E31E24

Blue: #0072BC

White backgrounds

Each ad must include:

“SALE NOW ON” banner at top

Our showroom address:
214 Upper Carrow Road, Fenwick Vale (must be fully visible, not cut off)

Phone number: 9482 1576

Our logo (provided)

Badge: “Celebrating 13 YEARS in Business” (must be clean and readable)

Call to Action:

For 5 ads: “Book a FREE quote TODAY!”

For Security Doors ad: “ORDER NOW”

Offers / Pricing:

Most products: “UP TO 40% OFF”

Plantation Shutters: “FROM $299/sqm”

Security Doors: “FROM $750”

Content for each ad (examples):

Veltrashade Blinds:

Made to Measure

Fully Installed

Wind, Sun & Insect Protection

Outdoor Awnings:

Reduce Heat & Glare

Energy Saving

Custom Made

Plantation Shutters:

Modern & Elegant

Light & Privacy Control

Durable & Easy Care

Roller Shutters:

Security Protection

Block Heat & Noise

Total Light Control

Security Doors:

3 Point Locking

Premium Mesh

Custom Made

Blinds & Sheers:

Huge Range of Fabrics

Modern Soft Finish

Perfect for Any Room

Important Notes:

All text must be sharp and easy to read (no blur)

Layout must be balanced and not overcrowded

Ensure no text is cut off (especially address and headings)

Badge text must be straight and professional (no distortion)

Use high-quality, relevant images (we will provide references)

Goal:
Create ads that look professional, trustworthy, and generate enquiries/bookings for in-home quotes.

We are open to creative ideas but want a strong, bold retail-style ad that converts.
I have uploaed chatgpt mocks

Target Market(s)

Homeowners in Melbourne, Australia (typically aged 30–65) looking to improve their homes with blinds, shutters, awnings and security doors. Mid to high income households focused on quality, security, and modern home upgrades.

Industry/Entity Type

Home Improvement / Construction / Retail

Font styles to use
Sans Serif

Requirements
Must have
• Clear, bold and easy-to-read text (must be readable on mobile) High-quality, non-blurry design Strong “SALE” style layout (retail promotional look) Proper spacing (no overcrowded designs) All key info visible (address must NOT be cut off) Correct pricing and offers included Clean “13 YEARS” badge (no distortion or curved text) Consistent branding across all 6 ads
Nice to have
• Modern, slightly premium feel while still being bold Good use of contrast (red/blue/white) Subtle shadows or layering to improve depth Clean use of icons or bullet points Strong hierarchy (headline → benefits → offer → CTA) Variations in layout for testing different ad styles
Should not have
• Minimal or plain designs (we want bold, sales-driven ads) Hard-to-read fonts or script fonts Low-quality or blurry images Overcrowded layouts with too much text Important text cut off (especially address or headings) Overuse of effects or “cheap” looking graphics Yellow-heavy colour schemes (must follow brand colours)

```html
<!DOCTYPE html>
<html lang="en">
<head>
<meta charset="UTF-8">
<title>Panes Screens &amp; Louvres – Veltrashade Blinds Sale</title>
<link rel="stylesheet" href="https://fonts.googleapis.com/css2?family=Arimo:wght@700&family=Montserrat:ital,wght@0,400;0,600;0,700;1,500;1,700;1,800&display=swap">
<style>
  :root {
    --brand-red: #E31E24;
    --brand-red-dark: #B3141A;
    --brand-blue: #0072BC;
    --ink: #1c1c1c;
    --canvas-bg: #F5F5F5;
    --white: #FFFFFF;
    --gold-light: #F7E08A;
    --gold-mid: #E2BE4E;
    --gold-dark: #B8902A;
    --rule: #E3262C;
  }
  * { box-sizing: border-box; margin: 0; padding: 0; }
  html, body { width: 1200px; height: 1200px; overflow: hidden; }
  body { background: var(--canvas-bg); font-family: "Montserrat", Arial, sans-serif; }

  .ad { position: relative; width: 1200px; height: 1200px; background: var(--canvas-bg); overflow: hidden; }

  .brand { position: absolute; left: 64px; top: 30px; display: flex; align-items: center; gap: 16px; }
  .brand-mark { width: 70px; height: 70px; background: var(--brand-blue); }
  .brand-name { font-family: "Montserrat", Arial, sans-serif; font-weight: 700; font-size: 34px; color: var(--brand-blue); letter-spacing: -0.5px; }

  .accent-block { position: absolute; left: 64px; top: 130px; width: 637px; height: 637px; background: var(--brand-blue); }

  .sale-banner {
    position: absolute; left: 106px; top: 172px; width: 890px; height: 95px;
    background: var(--brand-red); display: flex; align-items: center; padding-left: 28px; gap: 18px;
  }
  .sale-title { font-weight: 800; font-style: italic; font-size: 50px; color: var(--white); letter-spacing: 0.5px; }
  .sale-offer {
    font-weight: 800; font-style: italic; font-size: 40px; color: transparent;
    -webkit-text-stroke: 1.6px var(--white); letter-spacing: 0.5px;
  }

  .hero-photo {
    position: absolute; left: 106px; top: 267px; width: 989px; height: 564px;
    background: linear-gradient(180deg, #3b4049 0%, #4a5058 45%, #6f7a5a 70%, #c9c2b4 100%);
  }

  .anniversary-badge { position: absolute; left: 954px; top: 90px; width: 220px; height: 220px; }
  .anniversary-badge svg { position: absolute; inset: 0; }
  .badge-text {
    position: absolute; inset: 0; display: flex; flex-direction: column; align-items: center; justify-content: center;
    font-style: italic; font-weight: 500; font-size: 22px; line-height: 1.22; color: var(--ink); text-align: center;
  }
  .badge-text strong { font-weight: 800; font-size: 23px; }

  .product-title {
    position: absolute; left: 106px; top: 862px;
    font-family: "Arimo", Arial, sans-serif; font-weight: 700; font-size: 70px; color: var(--brand-blue); letter-spacing: 0.5px;
  }
  .title-rule { position: absolute; left: 106px; top: 951px; width: 989px; height: 2px; background: var(--rule); }

  .benefits { position: absolute; left: 106px; top: 975px; list-style: none; }
  .benefits li { display: flex; align-items: center; gap: 10px; font-size: 26px; line-height: 37px; color: var(--brand-blue); }
  .benefits svg { width: 24px; height: 24px; flex: none; }

  .cta {
    position: absolute; left: 789px; top: 989px; width: 308px; height: 87px;
    background: var(--brand-red); border-radius: 14px; box-shadow: 0 5px 0 var(--brand-red-dark);
    display: flex; align-items: center; justify-content: center; text-align: center;
    color: var(--white); font-weight: 700; font-size: 25px; line-height: 1.3;
  }

  .footer-bar {
    position: absolute; left: 0; top: 1111px; width: 1200px; height: 89px; background: var(--brand-blue);
    display: flex; align-items: center; justify-content: space-between; padding: 0 61px 0 64px;
    color: var(--white); font-size: 26px;
  }
</style>
</head>
<body>
<main class="ad">
  <header class="brand">
    <span class="brand-mark"></span>
    <span class="brand-name">Panes Screens &amp; Louvres</span>
  </header>

  <div class="accent-block"></div>

  <div class="hero-photo" role="img" aria-label="Outdoor patio under a pergola with dark charcoal zip screen blinds lowered, lounge sofa, potted plants and trees at sunset"></div>

  <div class="sale-banner">
    <span class="sale-title">SALE NOW ON</span>
    <span class="sale-offer">UP TO 40% OFF</span>
  </div>

  <div class="anniversary-badge">
    <svg viewBox="0 0 220 220" aria-hidden="true">
      <defs>
        <radialGradient id="goldFill" cx="40%" cy="35%" r="75%">
          <stop offset="0" stop-color="var(--gold-light)"/>
          <stop offset="0.6" stop-color="var(--gold-mid)"/>
          <stop offset="1" stop-color="var(--gold-dark)"/>
        </radialGradient>
      </defs>
      <g fill="url(#goldFill)">
        <rect x="32.2" y="32.2" width="155.6" height="155.6" transform="rotate(0 110 110)"/>
        <rect x="32.2" y="32.2" width="155.6" height="155.6" transform="rotate(15 110 110)"/>
        <rect x="32.2" y="32.2" width="155.6" height="155.6" transform="rotate(30 110 110)"/>
        <rect x="32.2" y="32.2" width="155.6" height="155.6" transform="rotate(45 110 110)"/>
        <rect x="32.2" y="32.2" width="155.6" height="155.6" transform="rotate(60 110 110)"/>
        <rect x="32.2" y="32.2" width="155.6" height="155.6" transform="rotate(75 110 110)"/>
      </g>
      <circle cx="110" cy="110" r="86" fill="url(#goldFill)" stroke="#FBF0C2" stroke-width="3"/>
    </svg>
    <div class="badge-text">
      <span>Celebrating</span>
      <strong>13 YEARS</strong>
      <span>in Business</span>
    </div>
  </div>

  <h1 class="product-title">VELTRASHADE BLINDS</h1>
  <div class="title-rule"></div>

  <ul class="benefits">
    <li><svg viewBox="0 0 24 24"><path d="M3 13l6 6L21 5" fill="none" stroke="#1c1c1c" stroke-width="3" stroke-linecap="round" stroke-linejoin="round"/></svg>Made to Measure</li>
    <li><svg viewBox="0 0 24 24"><path d="M3 13l6 6L21 5" fill="none" stroke="#1c1c1c" stroke-width="3" stroke-linecap="round" stroke-linejoin="round"/></svg>Fully Installed</li>
    <li><svg viewBox="0 0 24 24"><path d="M3 13l6 6L21 5" fill="none" stroke="#1c1c1c" stroke-width="3" stroke-linecap="round" stroke-linejoin="round"/></svg>Wind, Sun &amp; Insect Protection</li>
  </ul>

  <div class="cta">Book a FREE quote<br>TODAY!</div>

  <footer class="footer-bar">
    <span class="address">214 Upper Carrow Road, Fenwick Vale</span>
    <span class="phone">Phone number: 9482 1576</span>
  </footer>
</main>
</body>
</html>
```